Contemporary Business card for Event Manager

Needed for my startup events company in Melbourne. Events I manage will be based within the fashion industry, sporting events, product launches etc. Not weddings or small dinner parties. Therfore I am after something professional and aimed at high end corporate market; but with the added emphasis on not being too conservative or boring. I am happy with a pop of colour e.g. yellow or copper foil.

Target Market(s)

fashion industry, design industry, high end sporting events e.g. Polo, Grand Prix, corporate clients,

Industry/Entity Type

Fashion

Contact Information for Business Card

side 1
Lena Varsby (can be upper or lower case, have a feature full stop between first and surname, or at the end of the nameetc) I am open to ideas. I would also be fine with my initials or name as a logo on the front (if this is the case my full name would need to go on the second side of the card.
2nd side:
Mobile: +61 491 570 156
email: lena.varsby@mailtrove.com.au

on one side of the card:
event management | brand activation | Advisory Services

Font styles to use
Serif
Sans Serif

Requirements
Must have
• side 2 must have
• mobile number
• email address
• event management | brand activation | Advisory Services
• ** my full name (Lena Varsby) must be on the card somewhere)
Nice to have
• 1st side
• I see the card stock being either a dark grey, light grey, natural white or black (all matt colours on unprocessed card). I see the writing being copper foil, or foil white or foil black.
• To give you a feel for me, think: contemporary, minimalist, I love line drawings, concrete, white with grey vein marble, copper, white, grey, black...yes I do like colour....yellow (but pops of colour) ;) I would like the card to look designer but 'on trend' as I deal with a lot of design and fashion clients....styles - think the sophistication and simplicity of Morvane or urban contemporary.
• some examples of what I like. Although please don't leet this limit you...I really am happy to have something a little more urban or design focused like a line drawing of an object, person too or a photo image too.
• https://www.moodfolia.com/pin/100000000000000001/
• https://www.moodfolia.com/pin/100000000000000002/
• https://www.moodfolia.com/pin/100000000000000003/
• https://www.moodfolia.com/pin/10000000000000004/
• https://www.moodfolia.com/pin/10000000000000005/
• https://www.moodfolia.com/pin/10000000000000006/
• https://www.moodfolia.com/pin/100000000000000007/
• https://www.moodfolia.com/pin/100000000000000008/
• https://www.moodfolia.com/pin/100000000000000009/
Should not have
• should not look commercial or have cartoonish looking logos. However happy with a simple line drawing or logo with initials etc.

```html
<!DOCTYPE html>
<html lang="en">
<head>
<meta charset="utf-8">
<title>Lena Varsby — Business Card</title>
<link rel="stylesheet" href="https://fonts.googleapis.com/css2?family=Noto+Sans:wght@400;500&display=swap">
<style>
  :root {
    --backdrop: #5a3f27;
    --card-stock: #121212;
    --foil-yellow: #f6e200;
    --card-shadow: rgba(0, 0, 0, 0.45);
  }
  html, body {
    margin: 0;
    padding: 0;
    width: 1200px;
    height: 900px;
    overflow: hidden;
    background: var(--backdrop);
  }
  .canvas {
    position: relative;
    width: 1200px;
    height: 900px;
    font-family: "Noto Sans", "Verdana", sans-serif;
    color: var(--foil-yellow);
  }
  .card {
    position: absolute;
    width: 620px;
    height: 355px;
    background: var(--card-stock);
    box-shadow: 0 14px 30px var(--card-shadow);
  }
  .card--front { left: 100px; top: 80px; }
  .card--back  { left: 480px; top: 465px; }

  .front-mark {
    position: absolute;
    inset: 0;
    display: flex;
    align-items: center;
    justify-content: center;
    font-size: 46px;
    font-weight: 500;
    letter-spacing: 0.04em;
    text-transform: lowercase;
  }

  .contact-block {
    position: absolute;
    left: 150px;
    right: 30px;
    top: 138px;
    text-align: center;
    text-transform: uppercase;
    font-weight: 400;
  }
  .contact-block__name {
    margin: 0 0 10px;
    font-size: 27px;
    font-weight: 500;
    letter-spacing: 0.1em;
  }
  .contact-block__services {
    margin: 0 0 12px;
    font-size: 12.5px;
    letter-spacing: 0.1em;
    white-space: nowrap;
  }
  .contact-block__details {
    margin: 0;
    font-size: 12.5px;
    letter-spacing: 0.1em;
    white-space: nowrap;
  }
  .contact-block__details span + span { margin-left: 12px; }
</style>
</head>
<body>
  <main class="canvas">
    <section class="card card--front" aria-label="Card front">
      <div class="front-mark">Lena Varsby</div>
    </section>

    <section class="card card--back" aria-label="Card back">
      <div class="contact-block">
        <h1 class="contact-block__name">Lena Varsby</h1>
        <p class="contact-block__services">Event Management | Brand Activation | Advisory Services</p>
        <p class="contact-block__details">
          <span class="contact-block__phone">+61 491 570 156</span><span class="contact-block__email">lena.varsby@mailtrove.com.au</span>
        </p>
      </div>
    </section>
  </main>
</body>
</html>
```